Professional Business Cards for Janitorial Company

We are a Janitorial Company that services Commercial Buildings.

Our Logo is included. It can't look silly or cartoonish. Has to look professional.

Information:
Derek Malloy
Operations Manager
619.437.2086
DMalloy@BrightwayFacilityCare.com
www.BrightwayFacilityCare.com

```html
<!DOCTYPE html>
<html lang="en">
<head>
<meta charset="utf-8">
<title>Brightway Facility Care – Business Cards</title>
<link href="https://fonts.googleapis.com/css2?family=Open+Sans:wght@400;600;700&display=swap" rel="stylesheet">
<style>
  :root {
    --brand-blue: #1e5a96;
    --brand-blue-deep: #184d82;
    --steel-grey: #5b6066;
    --text-grey: #4a4f55;
    --card-white: #ffffff;
    --backdrop: #e6e7e9;
  }
  * { box-sizing: border-box; margin: 0; padding: 0; }
  html, body {
    width: 1200px; height: 872px; overflow: hidden;
    background: var(--backdrop);
    font-family: "Open Sans", Arial, sans-serif;
  }
  .card-sheet {
    width: 1200px; height: 872px;
    display: flex; align-items: center; justify-content: center; gap: 50px;
  }
  .card {
    position: relative;
    width: 525px; height: 300px;
    overflow: hidden;
    box-shadow: 0 6px 18px rgba(0,0,0,0.18);
  }
  /* Front */
  .card--front { background: var(--card-white); }
  .holder-name {
    position: absolute; left: 38px; top: 34px;
    color: var(--brand-blue);
    font-size: 25px; font-weight: 600; letter-spacing: 0.5px;
    text-transform: uppercase;
  }
  .holder-title {
    position: absolute; left: 38px; top: 70px;
    color: var(--text-grey);
    font-size: 17px; font-weight: 400;
  }
  .contact-list {
    position: absolute; left: 38px; top: 146px;
    list-style: none;
  }
  .contact-item {
    display: flex; align-items: center; gap: 9px;
    color: var(--text-grey);
    font-size: 13px; line-height: 25px;
  }
  .contact-icon {
    width: 15px; height: 15px; flex: none;
  }
  .brand-lockup {
    position: absolute; right: 34px; top: 172px;
    display: flex; align-items: center; gap: 10px;
  }
  .brand-mark {
    width: 22px; height: 22px; background: var(--brand-blue); flex: none;
  }
  .brand-name {
    color: var(--brand-blue);
    font-size: 17px; font-weight: 700; line-height: 1.15;
    width: 120px;
  }
  .card-band {
    position: absolute; left: 0; bottom: 0; width: 100%; height: 34px;
  }
  /* Back */
  .card--back { background: var(--brand-blue); }
  .back-lockup {
    position: absolute; left: 50%; top: 50%;
    transform: translate(-50%, -58%);
    display: flex; align-items: center; gap: 16px;
  }
  .back-lockup .brand-mark { width: 40px; height: 40px; background: var(--card-white); }
  .back-lockup .brand-name {
    color: var(--card-white); font-size: 28px; width: 220px;
  }
  .back-rule {
    position: absolute; left: 130px; right: 60px; top: 196px;
    height: 5px; background: var(--card-white);
  }
</style>
</head>
<body>
<main class="card-sheet">

  <section class="card card--front" aria-label="Business card front">
    <h1 class="holder-name">Derek Malloy</h1>
    <p class="holder-title">Operations manager</p>

    <ul class="contact-list">
      <li class="contact-item">
        <svg class="contact-icon" viewBox="0 0 16 16" aria-hidden="true">
          <circle cx="8" cy="8" r="7.5" fill="#4a4f55"/>
          <path d="M5.3 4.2l1.3-.3.8 1.9-.9.7c.4.9 1.1 1.6 2 2l.7-.9 1.9.8-.3 1.3c-3 .2-5.7-2.5-5.5-5.5z" fill="#fff"/>
        </svg>
        619.437.2086
      </li>
      <li class="contact-item">
        <svg class="contact-icon" viewBox="0 0 16 16" aria-hidden="true">
          <circle cx="8" cy="8" r="7.5" fill="#4a4f55"/>
          <rect x="4" y="5.3" width="8" height="5.4" fill="#fff"/>
          <path d="M4 5.3l4 3 4-3" fill="none" stroke="#4a4f55" stroke-width="0.9"/>
        </svg>
        DMalloy@BrightwayFacilityCare.com
      </li>
      <li class="contact-item">
        <svg class="contact-icon" viewBox="0 0 16 16" aria-hidden="true">
          <circle cx="8" cy="8" r="7.5" fill="#4a4f55"/>
          <g fill="none" stroke="#fff" stroke-width="0.9">
            <circle cx="8" cy="8" r="4"/>
            <ellipse cx="8" cy="8" rx="1.7" ry="4"/>
            <path d="M4 8h8"/>
          </g>
        </svg>
        www.BrightwayFacilityCare.com
      </li>
    </ul>

    <div class="brand-lockup">
      <span class="brand-mark"></span>
      <span class="brand-name">Brightway Facility Care</span>
    </div>

    <svg class="card-band" viewBox="0 0 525 34" preserveAspectRatio="none" aria-hidden="true">
      <polygon points="0,10 200,10 224,34 0,34" fill="var(--brand-blue)"/>
      <polygon points="200,10 525,10 525,34 224,34" fill="var(--steel-grey)"/>
      <polygon points="186,10 200,10 224,34 210,34" fill="#ffffff"/>
    </svg>
  </section>

  <section class="card card--back" aria-label="Business card back">
    <div class="back-lockup">
      <span class="brand-mark"></span>
      <span class="brand-name">Brightway Facility Care</span>
    </div>
    <div class="back-rule"></div>
  </section>

</main>
</body>
</html>
```